Organic Mavu (Coffee) Scrub Label for high end product

Need a product label for a coffee based body scrub called Mavu Body Scrub a 100% organic product. Our primary target is the yoga community so designs should reflect calm, perhaps incorporate eastern yoga symbology. simpler the better. Design should include both a round lid label and a rectangular wrap around label.

Target Market(s)

yoga community, people with cellulite, etc.

Industry/Entity Type

Community

```html
<!DOCTYPE html>
<html lang="en">
<head>
<meta charset="utf-8">
<title>Mavu Body Scrub – Wrap Label</title>
<link rel="stylesheet" href="https://fonts.googleapis.com/css2?family=Open+Sans:wght@400&family=Satisfy&display=swap">
<style>
  :root {
    --page-bg: #ecebe8;
    --label-cream: #f8f6f1;
    --pattern-tone: #efebe3;
    --sage: #7fa57a;
    --mauve: #9c7b7c;
    --cocoa: #8b7670;
    --bean-dark: #4a2a18;
    --bean-mid: #7a4a2c;
  }
  * { margin: 0; padding: 0; box-sizing: border-box; }
  html, body {
    width: 1200px;
    height: 1200px;
    overflow: hidden;
    background: var(--page-bg);
  }
  .canvas {
    position: relative;
    width: 1200px;
    height: 1200px;
  }
  .wrap-label {
    position: absolute;
    left: 70px;
    top: 116px;
    width: 1060px;
    height: 968px;
    background: var(--label-cream);
    overflow: hidden;
    box-shadow: 0 6px 24px rgba(0, 0, 0, 0.08);
  }
  .bean-pattern {
    position: absolute;
    inset: 0;
    background: radial-gradient(ellipse at 50% 45%, var(--label-cream) 0%, var(--pattern-tone) 100%);
  }
  .label-copy {
    position: absolute;
    left: 0;
    right: 0;
    top: 0;
    text-align: center;
    color: var(--cocoa);
  }
  .organic-tag {
    position: absolute;
    left: 0; right: 0;
    top: 160px;
    font-family: "Open Sans", sans-serif;
    font-size: 42px;
    color: var(--sage);
    letter-spacing: 0.5px;
  }
  .product-name {
    position: absolute;
    left: 0; right: 0;
    top: 230px;
    font-family: "Satisfy", cursive;
    font-size: 150px;
    line-height: 1.2;
    color: var(--mauve);
  }
  .product-type {
    position: absolute;
    left: 0; right: 0;
    top: 470px;
    font-family: "Open Sans", sans-serif;
    font-size: 42px;
    color: var(--sage);
  }
  .benefits {
    position: absolute;
    left: 160px; right: 160px;
    top: 532px;
    font-family: "Open Sans", sans-serif;
    font-size: 15px;
    line-height: 22px;
    text-transform: uppercase;
    color: var(--cocoa);
  }
  .volume {
    position: absolute;
    left: 0; right: 0;
    top: 652px;
    font-family: "Open Sans", sans-serif;
    font-size: 57px;
    color: var(--cocoa);
  }
  .bean-border {
    position: absolute;
    left: 0;
    right: 0;
    bottom: 0;
    height: 268px;
    background: linear-gradient(to bottom, rgba(122, 74, 44, 0) 0%, rgba(122, 74, 44, 0.55) 30%, var(--bean-mid) 55%, var(--bean-dark) 100%);
  }
</style>
</head>
<body>
  <main class="canvas">
    <section class="wrap-label">
      <div class="bean-pattern" role="img" aria-label="Faint line-drawn coffee bean pattern across the label background"></div>
      <div class="label-copy">
        <p class="organic-tag">100% Organic Product</p>
        <h1 class="product-name">Mavu Scrub</h1>
        <p class="product-type">BODY SCRUB</p>
        <p class="benefits">Increase blood circulation, great exfoliator, prevents ingrown hair and has<br>anti-aging and anti cellulite properties</p>
        <p class="volume">300ml</p>
      </div>
      <div class="bean-border" role="img" aria-label="Photograph of roasted coffee beans scattered along the bottom edge"></div>
    </section>
  </main>
</body>
</html>
```